Advertising poster for podcast event

"The Lantern Table" is one of the most popular podcasts in Switzerland (https://listen.brovakast.example/show/4kqPLmWX317TRvbnQ8ZsHD). It is hosted by the two radio DJs Lukas Brandt and Adrian Furrer. For a series of live shows where the podcast is recorded with an audience, we need a design of a poster. This should have the format A3 high. In addition, the image must be used that was uploaded here, because this is the cover photo with which you can always recognize the podcast. But what is designed around it is up to you. In addition, it must contain the following text:

- Title of the event:
The lantern table - Live
- Show dates:
Saturday, November 11, 2023 - Solothurn
Wednesday, December 27, 2023 - Berne
Thursday, December 28, 2023 - Berne
- A line with additional information about the presale:
The pavilion, information and tickets: www.diekuppel.example

Target Market(s)

Switzerland

Industry/Entity Type

Entertainment

Requirements
Must have
• The attached image and text according to the briefing.

```html
<!DOCTYPE html>
<html lang="en">
<head>
<meta charset="utf-8">
<title>The Lantern Table – Live Poster</title>
<link href="https://fonts.googleapis.com/css2?family=Bebas+Neue&display=swap" rel="stylesheet">
<style>
  :root {
    --page-bg: #eeeeee;
    --ink: #262624;
    --cream: #f1dba6;
    --orange: #f06c22;
    --taupe: #8b7f6b;
    --white: #ffffff;
  }
  html, body {
    margin: 0;
    padding: 0;
    width: 1200px;
    height: 1200px;
    overflow: hidden;
    background: var(--page-bg);
    font-family: "Bebas Neue", "Oswald", sans-serif;
  }
  .canvas { position: relative; width: 1200px; height: 1200px; }
  .poster {
    position: absolute; left: 205px; top: 45px; width: 789px; height: 1110px;
    background: var(--ink); overflow: hidden;
  }
  .frame-cream {
    position: absolute; left: 28px; top: 36px; width: 733px; height: 1042px;
    background: var(--cream);
  }
  .frame-inner {
    position: absolute; left: 42px; top: 51px; width: 704px; height: 1011px;
    background: var(--ink);
  }
  .cover-art {
    position: absolute; left: 57px; top: 222px; width: 666px; height: 409px;
    background: linear-gradient(180deg, #2b2a27 0%, #f06c22 40%, #f4efe6 75%, #d9c7a0 100%);
    clip-path: polygon(0 93px, 100% 0, 100% 100%, 0 100%);
  }
  .header-art { position: absolute; left: 0; top: 0; }
  .title-dot {
    position: absolute; width: 22px; height: 22px; border-radius: 50%;
    background: var(--cream);
  }
  .title-dot.left { left: 67px; top: 127px; }
  .title-dot.right { left: 256px; top: 99px; }
  .title-small {
    position: absolute; left: 110px; top: 63px; margin: 0;
    font-size: 107px; line-height: 1; font-weight: 400; color: var(--white);
  }
  .title-main {
    position: absolute; left: 88px; top: 200px; margin: 0;
    font-size: 90px; line-height: 1; font-weight: 400; color: var(--white);
    white-space: nowrap;
  }
  .dates-panel {
    position: absolute; left: 65px; top: 638px; width: 657px; height: 416px;
    background: var(--orange); text-align: center;
  }
  .dates-heading {
    position: absolute; left: 0; top: 7px; width: 100%; margin: 0;
    display: flex; align-items: center; justify-content: center; gap: 18px;
    font-size: 62px; line-height: 1; font-weight: 400; color: var(--ink);
  }
  .speed-lines { display: flex; flex-direction: column; gap: 5px; }
  .speed-lines span { display: block; height: 3px; background: var(--ink); }
  .speed-lines.left { align-items: flex-end; }
  .speed-lines.right { align-items: flex-start; }
  .show-list { list-style: none; margin: 0; padding: 0; }
  .show-date {
    position: absolute; left: 0; width: 100%;
    font-size: 44px; line-height: 1; letter-spacing: 0.5px; color: var(--white);
    white-space: nowrap;
  }
  .show-date.first { top: 92px; }
  .show-date.second { top: 182px; }
  .show-date.third { top: 272px; }
  .star-sep {
    position: absolute; left: 313px; width: 31px; height: 30px;
  }
  .star-sep.one { top: 143px; }
  .star-sep.two { top: 233px; }
  .presale-bar {
    position: absolute; left: 11px; top: 345px; width: 634px; height: 40px; margin: 0;
    background: var(--ink); color: var(--white);
    display: flex; align-items: center; justify-content: center; gap: 10px;
    font-size: 26px; line-height: 1; white-space: nowrap;
  }
  .presale-bar .dot { width: 11px; height: 11px; border-radius: 50%; background: var(--cream); }
</style>
</head>
<body>
<div class="canvas">
  <div class="poster">
    <div class="frame-cream"></div>
    <div class="frame-inner"></div>

    <div class="cover-art" role="img" aria-label="Podcast cover illustration: the two hosts beside a vintage microphone in front of an audio waveform"></div>

    <svg class="header-art" width="789" height="400" viewBox="0 0 789 400" aria-hidden="true">
      <polygon points="57,67 731,67 731,101 57,194" fill="var(--taupe)"/>
      <polygon points="79,200 712,107 712,222 79,315" fill="var(--orange)"/>
    </svg>

    <span class="title-dot left"></span>
    <span class="title-dot right"></span>
    <h1 class="title-small">THE</h1>
    <p class="title-main">LANTERN TABLE - LIVE</p>

    <section class="dates-panel">
      <h2 class="dates-heading">
        <span class="speed-lines left"><span style="width:68px"></span><span style="width:48px"></span><span style="width:68px"></span></span>
        SHOW DATES
        <span class="speed-lines right"><span style="width:68px"></span><span style="width:48px"></span><span style="width:68px"></span></span>
      </h2>
      <ul class="show-list">
        <li class="show-date first">SATURDAY, NOVEMBER 11, 2023 - SOLOTHURN</li>
        <li class="show-date second">WEDNESDAY, DECEMBER 27, 2023 - BERNE</li>
        <li class="show-date third">THURSDAY, DECEMBER 28, 2023 - BERNE</li>
      </ul>
      <svg class="star-sep one" viewBox="0 0 24 23" aria-hidden="true"><polygon points="12,0 15,8.5 24,8.5 16.8,13.8 19.4,22.5 12,17.3 4.6,22.5 7.2,13.8 0,8.5 9,8.5" fill="var(--ink)"/></svg>
      <svg class="star-sep two" viewBox="0 0 24 23" aria-hidden="true"><polygon points="12,0 15,8.5 24,8.5 16.8,13.8 19.4,22.5 12,17.3 4.6,22.5 7.2,13.8 0,8.5 9,8.5" fill="var(--ink)"/></svg>
      <p class="presale-bar"><span class="dot"></span>THE PAVILION, INFORMATION AND TICKETS: WWW.DIEKUPPEL.EXAMPLE<span class="dot"></span></p>
    </section>
  </div>
</div>
</body>
</html>
```